Coralith Partners's New Branding
Anything the customer sees, we want to update
Coralith Partners's New Branding -
Creative Brief
Professional
Dorian Pelk, MCP
Director of Technology
418 West Alder Road Brelton, KS 66218
dorian.pelk@coralithpt.example
www.coralithpt.example
In addition to branding our business cards, we're also looking to brand: 1) folders - two pockets w/ a slotted area on the left pocket to insert a business card 2) brochures - 8.5"x11" tri-fold brochure 3) letterhead 4) envelopes 5) sales proposal cover letter - Our logo and name - Presented to: "Customer's name" - Presented by: "our sales person(s)" - Title of presentation - our web address 6) powerpoint 7) binders (including spline) 8) cd label - Company's name we're presenting cd to - our logo and name - title of content on cd
Quote: "Our work keeps yours growing" Please layout the quote so that if we put a QR code on the back of the card in the future, it won't look out of place.

```html
<!DOCTYPE html>
<html lang="en">
<head>
<meta charset="utf-8">
<title>Coralith Partners Business Card</title>
<link rel="stylesheet" href="https://fonts.googleapis.com/css2?family=Tinos:wght@400;700&display=swap">
<style>
  :root {
    --backdrop: #ecebe7;
    --green-deep: #0e3f26;
    --green-mid: #1a6a40;
    --green-text: #2e7d3a;
    --green-accent: #3c9a44;
    --ink-grey: #4a4a4a;
    --paper: #ffffff;
    --white: #ffffff;
  }
  html, body {
    margin: 0;
    padding: 0;
    width: 1200px;
    height: 869px;
    overflow: hidden;
    background: var(--backdrop);
    font-family: "Tinos", "Times New Roman", serif;
  }
  .canvas {
    position: relative;
    width: 1200px;
    height: 869px;
  }
  .card {
    position: absolute;
    top: 254px;
    height: 298px;
    box-shadow: 0 2px 6px rgba(0,0,0,0.25);
    box-sizing: border-box;
  }
  .card-back {
    left: 67px;
    width: 516px;
    background: radial-gradient(ellipse at 60% 45%, var(--green-mid) 0%, var(--green-deep) 75%);
    color: var(--white);
  }
  .card-back .quote {
    position: absolute;
    top: 136px;
    left: 0;
    width: 100%;
    margin: 0;
    text-align: center;
    font-size: 20px;
    letter-spacing: 0.2px;
  }
  .card-back .web {
    position: absolute;
    bottom: 14px;
    left: 0;
    width: 100%;
    margin: 0;
    text-align: center;
    font-size: 12px;
  }
  .card-front {
    left: 638px;
    width: 497px;
    background: var(--paper);
    border: 2px solid var(--green-accent);
  }
  .brand {
    position: absolute;
    top: 50px;
    left: 0;
    width: 100%;
    display: flex;
    justify-content: center;
    align-items: center;
    gap: 12px;
  }
  .brand-dot {
    width: 38px;
    height: 38px;
    border-radius: 50%;
    background: var(--green-mid);
  }
  .brand-name {
    font-size: 30px;
    color: var(--ink-grey);
    letter-spacing: 1px;
  }
  .person {
    position: absolute;
    top: 148px;
    left: 0;
    width: 100%;
    text-align: center;
    color: var(--green-text);
  }
  .person .name { font-size: 23px; line-height: 26px; }
  .person .role { font-size: 15px; line-height: 20px; }
  .contact {
    position: absolute;
    top: 236px;
    font-size: 11px;
    line-height: 13px;
    color: var(--green-accent);
  }
  .contact-left { left: 18px; }
  .contact-left .email { margin-top: 8px; }
  .contact-right { right: 18px; text-align: right; }
  .contact-right span { color: var(--ink-grey); }
</style>
</head>
<body>
<main class="canvas">
  <section class="card card-back">
    <p class="quote">Our work keeps yours growing</p>
    <p class="web">www.coralithpt.example</p>
  </section>

  <section class="card card-front">
    <div class="brand">
      <div class="brand-dot"></div>
      <div class="brand-name">Coralith Partners</div>
    </div>
    <div class="person">
      <div class="name">Dorian Pelk, MCP</div>
      <div class="role">Director of Technology</div>
    </div>
    <div class="contact contact-left">
      <div>418 West Alder Road</div>
      <div>Brelton, KS 66218</div>
      <div class="email">dorian.pelk@coralithpt.example</div>
    </div>
    <div class="contact contact-right">
      <div><span>cell:</span> (555) 010-0147</div>
      <div><span>phone:</span> (555) 010-0182</div>
      <div><span>fax:</span> (555) 010-0163</div>
    </div>
  </section>
</main>
</body>
</html>
```